Commercial Real Estate Appraisal Company needs a postcard design

We need a postcard design for a commercial real estate company based out of Ballston Lake, New York called "Northfield Appraisers".

Northfield Appraisers, LLC., provides high quality commercial appraisal and real estate consulting services to our clients. Our company provides appraisal services for financial lending institutions, real estate developers, local municipalities, attorney’s, private individuals and businesses. Significant capital expenditures were made to ensure we can provide top of the line data research and research publications, as well as, generate our reports with industry leading appraisal software for increased accuracy and efficiency.

Services we provide

Advisory & Consulting Services, Net Lease Valuation, Capitalization Rate Consultation, Operating Expense Consultation, Discounted Cash Flow Analysis, Portfolio Valuation, Expert Witness Services, Property and Comparable Analyses, Financial Feasibility Studies, Property Tax Services, Going Concern Valuations, Real Estate Due Diligence Analyses, Highest and Best Use Studies, Real Estate Valuation, Lease Versus Purchase Analyses, Rent Arbitration and Consultation, Market Rent Analyses, Sale Lease-Backs Analysis, Market Studies, Site Inspections, Divorce Proceedings, Probate / Estate Matters

Please save room on the card for postage and addressing

Industry/Entity Type

Real Estate

```html
<!DOCTYPE html>
<html lang="en">
<head>
<meta charset="utf-8">
<title>Northfield Appraisers – Postcard</title>
<link href="https://fonts.googleapis.com/css2?family=Tinos:wght@400;700&display=swap" rel="stylesheet">
<style>
  :root {
    --page-bg: #d9d9db;
    --card-bg: #ffffff;
    --ink: #1a1a1a;
    --brand-ink: #1c1b33;
    --mark-fill: #e3e3ea;
    --rule: #a9a9a9;
    --stamp-line: #8a8a8a;
  }
  * { margin: 0; padding: 0; box-sizing: border-box; }
  html, body {
    width: 1200px;
    height: 1000px;
    overflow: hidden;
    background: var(--page-bg);
  }
  .postcard {
    position: absolute;
    left: 50px;
    top: 147px;
    width: 1100px;
    height: 708px;
    background: var(--card-bg);
    font-family: "Tinos", "Times New Roman", serif;
    color: var(--ink);
  }
  .brand-mark {
    position: absolute;
    left: 153px;
    top: 38px;
    width: 150px;
    height: 150px;
    border-radius: 50%;
    background: var(--mark-fill);
  }
  .brand-name {
    position: absolute;
    left: 40px;
    top: 207px;
    width: 388px;
    font-size: 29px;
    font-weight: 400;
    letter-spacing: 0.4px;
    text-transform: uppercase;
    color: var(--brand-ink);
    white-space: nowrap;
    line-height: 1;
  }
  .brand-tagline {
    position: absolute;
    left: 57px;
    top: 240px;
    width: 350px;
    font-size: 11px;
    letter-spacing: 2.6px;
    text-transform: uppercase;
    color: var(--brand-ink);
    white-space: nowrap;
    line-height: 1;
  }
  .contact {
    position: absolute;
    left: 40px;
    top: 300px;
    font-size: 18px;
    line-height: 21.5px;
    font-style: normal;
  }
  .services-heading {
    position: absolute;
    left: 40px;
    top: 431px;
    font-size: 20px;
    font-weight: 700;
  }
  .services-list {
    position: absolute;
    left: 40px;
    top: 476px;
    width: 522px;
    font-size: 17.5px;
    line-height: 21.5px;
  }
  .services-line {
    display: block;
    white-space: nowrap;
    text-align: justify;
    text-align-last: justify;
  }
  .services-line:last-child {
    text-align-last: left;
  }
  .stamp-box {
    position: absolute;
    left: 927px;
    top: 10px;
    width: 164px;
    height: 161px;
    border: 1px dashed var(--stamp-line);
  }
  .address-lines {
    position: absolute;
    left: 619px;
    top: 335px;
    width: 470px;
  }
  .address-line {
    height: 1px;
    background: var(--rule);
    margin-bottom: 46.5px;
  }
</style>
</head>
<body>
  <section class="postcard">
    <div class="brand-mark" role="img" aria-label="Company logo mark area"></div>
    <h1 class="brand-name">Northfield Appraisers</h1>
    <p class="brand-tagline">Real Estate Appraisers &amp; Consultants</p>

    <address class="contact">
      Your Company Address Here<br>
      Street, City, Pos Code, Etc.<br>
      Your email@companyname.com<br>
      www.yourwebsite.com
    </address>

    <h2 class="services-heading">Our Services:</h2>
    <p class="services-list">
      <span class="services-line">Advisory &amp; Consulting Services, Net Lease Valuation, Capitalization</span>
      <span class="services-line">Rate Consultation, Operating Expense Consultation, Discounted Cash</span>
      <span class="services-line">Flow Analysis, Portfolio Valuation, Expert Witness Services, Property</span>
      <span class="services-line">and Comparable Analyses, Financial Feasibility Studies, Property Tax</span>
      <span class="services-line">Services, Going Concern Valuations, Real Estate Due Diligence Analy-</span>
      <span class="services-line">ses, Highest and Best Use Studies, Real Estate Valuation, Lease Versus</span>
      <span class="services-line">Purchase Analyses, Rent Arbitration and Consultation, Market Rent</span>
      <span class="services-line">Analyses, Sale Lease-Backs Analysis, Market Studies, Site Inspections,</span>
      <span class="services-line">Divorce Proceedings, Probate / Estate Matters</span>
    </p>

    <div class="stamp-box" aria-label="Postage stamp area"></div>

    <div class="address-lines" aria-label="Recipient address lines">
      <div class="address-line"></div>
      <div class="address-line"></div>
      <div class="address-line"></div>
      <div class="address-line"></div>
    </div>
  </section>
</body>
</html>
```